Vemtra Group: Business Card for a high end technology company

We need a cool new design for our business cards using our cloud logo. We are a technology consulting business. We pride ourselves on be the best of the best. We mainly focus on cloud solutions and managed services. We need a business card that sets us apart from the other technology companies in the area and allows us to stand out.

Target Market(s)

Technology departments, CIO, CEOs, and Information Technology Staff.

Industry/Entity Type

Information Technology

Contact Information for Business Card

Must have the logo and our name.
Must have employee name, email address, office phone, cell phone and website.
Need to have all info on one side a cool design on backside.

Font styles to use
Serif
Sans Serif

Requirements
Must have
• Must have the logo and our name.
• Must have employee name, email address, office phone, cell phone and website.
• Need to have all info on one side a cool design on back side.
• Must be a crisp clean design, not too busy or confusing.

```html
<!DOCTYPE html>
<html lang="en">
<head>
<meta charset="utf-8">
<title>Vemtra Group — Business Card</title>
<link rel="stylesheet" href="https://fonts.googleapis.com/css2?family=Lato:wght@300;400;700;900&display=swap">
<style>
  :root {
    --brand-blue: #0f72b9;
    --ink: #232323;
    --band-dark: #252525;
    --paper: #ffffff;
    --backdrop: #d9d9d9;
    --muted: #3a3a3a;
  }
  * { box-sizing: border-box; margin: 0; padding: 0; }
  html, body { width: 1200px; height: 900px; overflow: hidden; }
  body {
    background: var(--backdrop);
    font-family: "Lato", Arial, sans-serif;
    color: var(--ink);
    display: flex;
    flex-direction: column;
    align-items: center;
    justify-content: center;
    gap: 40px;
  }
  .card {
    position: relative;
    width: 680px;
    height: 388px;
    background: var(--paper);
    overflow: hidden;
    box-shadow: 0 6px 18px rgba(0,0,0,0.18);
  }
  .card__art { position: absolute; inset: 0; }

  /* Front */
  .front__brand {
    position: absolute; left: 48px; top: 38px;
    font-size: 48px; font-weight: 400; letter-spacing: 0.5px;
    color: var(--ink);
  }
  .front__person {
    position: absolute; right: 40px; top: 138px; text-align: right;
  }
  .person__name { font-weight: 900; font-size: 19px; letter-spacing: 0.4px; }
  .person__role { font-weight: 400; font-size: 14px; letter-spacing: 0.3px; text-transform: uppercase; }
  .contacts {
    position: absolute; left: 44px; top: 222px;
    display: grid; grid-template-columns: 210px 220px; row-gap: 12px; column-gap: 20px;
    font-size: 17px; color: var(--muted);
  }
  .contact { display: flex; align-items: center; gap: 14px; }
  .contact svg { width: 16px; height: 16px; flex: none; fill: var(--brand-blue); }
  .address {
    position: absolute; left: 44px; top: 312px;
    display: flex; align-items: center; gap: 16px;
    color: var(--paper); font-size: 17px;
  }
  .address svg { width: 16px; height: 18px; fill: var(--paper); }

  /* Back */
  .back__brand {
    position: absolute; left: 50%; top: 50%;
    transform: translate(-50%, -58%);
    display: flex; flex-direction: column; align-items: center; gap: 8px;
  }
  .brand-lockup { display: flex; align-items: center; gap: 14px; }
  .brand-lockup__dot { width: 30px; height: 30px; border-radius: 50%; background: var(--brand-blue); }
  .brand-lockup__name { font-size: 40px; font-weight: 400; color: var(--ink); }
  .back__url { font-size: 13px; font-weight: 700; letter-spacing: 0.5px; color: var(--ink); }
</style>
</head>
<body>

  <section class="card card--front" aria-label="Business card front">
    <svg class="card__art" viewBox="0 0 680 388" aria-hidden="true">
      <rect x="0" y="148" width="420" height="6" fill="var(--brand-blue)"/>
      <polygon points="420,126 680,126 680,132 414,132" fill="var(--band-dark)"/>
      <rect x="0" y="340" width="680" height="48" fill="var(--brand-blue)"/>
      <rect x="420" y="310" width="260" height="30" fill="var(--brand-blue)"/>
      <path d="M0,302 L400,302 Q410,272 430,272 L470,272 Q482,272 490,282 L530,340 L0,340 Z" fill="var(--band-dark)"/>
    </svg>

    <div class="front__brand">Vemtra Group</div>

    <div class="front__person">
      <div class="person__name">DORIAN KESSEL</div>
      <div class="person__role">Graphic Designer</div>
    </div>

    <div class="contacts">
      <div class="contact">
        <svg viewBox="0 0 16 16"><path d="M3.6 1 6 3.6 4.8 5.6c.9 2 2.5 3.7 4.6 4.6l2-1.2L14 11.4 12.6 14C6.4 14 2 9.6 2 3.4z"/></svg>
        <span>+1 415 555 0142</span>
      </div>
      <div class="contact">
        <svg viewBox="0 0 16 16"><path d="M1 2h14v9H9.5l.5 2h2v1H4v-1h2l.5-2H1zm1.3 1.3v6.4h11.4V3.3z"/></svg>
        <span>www.vemtragroup.com</span>
      </div>
      <div class="contact">
        <svg viewBox="0 0 16 16"><path d="M4 0h8a1 1 0 0 1 1 1v14a1 1 0 0 1-1 1H4a1 1 0 0 1-1-1V1a1 1 0 0 1 1-1zm.4 1.6v11h7.2v-11zM7 13.5v1h2v-1z"/></svg>
        <span>+1 415 555 0187</span>
      </div>
      <div class="contact">
        <svg viewBox="0 0 16 16"><path d="M1 3h14v1.2L8 8.6 1 4.2zm0 2.6 7 4.4 7-4.4V13H1z"/></svg>
        <span>info@vemtragroup.com</span>
      </div>
    </div>

    <div class="address">
      <svg viewBox="0 0 16 18"><path d="M8 0a6 6 0 0 1 6 6c0 4.4-6 12-6 12S2 10.4 2 6a6 6 0 0 1 6-6zm0 3.5A2.5 2.5 0 1 0 8 8.5 2.5 2.5 0 0 0 8 3.5z"/></svg>
      <span>48 Larkspur Avenue, Denver 80203, USA</span>
    </div>
  </section>

  <section class="card card--back" aria-label="Business card back">
    <svg class="card__art" viewBox="0 0 680 388" aria-hidden="true">
      <rect x="0" y="0" width="680" height="50" fill="var(--brand-blue)"/>
      <rect x="0" y="50" width="680" height="14" fill="var(--band-dark)"/>
      <rect x="0" y="278" width="680" height="14" fill="var(--band-dark)"/>
      <rect x="0" y="292" width="680" height="96" fill="var(--brand-blue)"/>
    </svg>

    <div class="back__brand">
      <div class="brand-lockup">
        <span class="brand-lockup__dot"></span>
        <span class="brand-lockup__name">Vemtra Group</span>
      </div>
      <div class="back__url">www.vemtragroup.com</div>
    </div>
  </section>

</body>
</html>
```